Website for Company to help with House Restoration from Hurricane Damage

Crisp, Clean and Professional!

I need a FRONT page for a website. I need it created in photoshop with the layers intact. We DO NOT need the HTML or RBT for the site. Simply the design. Any fonts you use will need to be included if they are not standard. Please make sure any fonts you use in the body of the text are available for use on Google Fonts.

I have attached a word doc that lists the menu items and additional instructions.

A little about the company - after Hurricane Quintessa - RBT developed a system which allows the house to be raised, the Pylonets installed, and the house reset on the Pylonets without the expense of moving the house or driving new pilings. This option can be installed in a matter of days with limited space and at a lower construction cost.

Please refer to the attached musthaves.doc and images that are included.

The main page must incorporate the menu, the attached photos w/ text underneath (text is in the word doc attached), and the text included in the word doc.

Standard footer with contact info as well.

If you have questions please contact us!
Updates

Designs are due by Friday! We will pick one this weekend.  We are unable to change it from 10 days to 5.  Thank you!!!

Target Market(s)

People who lost their homes or businesses due to a hurricane.

Industry/Entity Type

Construction

Requirements
Must have
• See attached musthaves.doc

```html
<!DOCTYPE html>
<html lang="en">
<head>
<meta charset="utf-8">
<title>RBT — Rebuild Safer, Stronger, Better</title>
<link href="https://fonts.googleapis.com/css2?family=Montserrat:wght@400;500;600&family=Open+Sans:wght@400;600&display=swap" rel="stylesheet">
<style>
:root{
  --bar-light:#f2f2f2;
  --bar-edge:#e2e2e2;
  --nav-top:#7f9a5a;
  --nav-bottom:#5a7236;
  --logo-bg:#dbe9c6;
  --logo-ink:#3e5a22;
  --ink:#3f3f3f;
  --body:#5a5a5a;
  --muted:#c9c9c9;
  --accent:#d8261f;
  --footer:#6e854a;
  --footer-dark:#4e6132;
  --orange:#e8952a;
  --white:#ffffff;
}
*{margin:0;padding:0;box-sizing:border-box}
html,body{width:1019px;height:1200px;overflow:hidden;background:var(--white)}
body{font-family:"Montserrat",Arial,sans-serif;color:var(--body)}
.page{position:relative;width:1000px;height:1178px;transform:scale(1.019,1.0187);transform-origin:0 0}
.abs{position:absolute}

/* header */
.topbar{left:0;top:0;width:1000px;height:48px;background:linear-gradient(var(--white),var(--bar-light));border-bottom:1px solid var(--bar-edge)}
.contact-item{top:14px;display:flex;align-items:center;gap:12px;font-size:10.5px;color:var(--ink)}
.contact-item svg{display:block}
.mainnav{left:0;top:48px;width:1000px;height:30px;background:linear-gradient(var(--nav-top),var(--nav-bottom));border-top:1px solid #9bb37a}
.mainnav ul{position:absolute;left:286px;top:0;display:flex;list-style:none;height:30px}
.mainnav li{font-size:10.3px;font-weight:500;color:var(--white);padding:0 7px;line-height:30px;border-left:1px solid rgba(0,0,0,.15);box-shadow:inset 1px 0 rgba(255,255,255,.12)}
.mainnav li:first-child{border-left:none;box-shadow:none}
.brand{left:173px;top:0;width:99px;height:100px;background:var(--logo-bg);border:2px solid #f4f9ec;box-shadow:0 1px 4px rgba(0,0,0,.35);display:flex;align-items:center;justify-content:center;font-size:30px;font-weight:600;color:var(--logo-ink);z-index:3}

/* hero */
.hero{left:0;top:78px;width:1000px;height:300px;background:linear-gradient(180deg,#74708d 0%,#b08c98 14%,#e5a07a 20%,#a49aa8 24%,#8f8ba0 40%,#7e7a90 62%,#6c6275 80%,#564c5d 100%)}

/* intro panel */
.panel{left:172px;top:336px;width:657px;height:260px;background:linear-gradient(#f1f1f1,var(--white) 70px);border-radius:6px 6px 0 0}
.panel-title{left:187px;top:348px;font-size:16.2px;font-weight:500;color:var(--ink);letter-spacing:.2px}
.rule{left:187px;top:380px;width:404px;height:1px;background:#d8d8d8}
.intro{left:187px;top:389px;width:406px;font-size:10.1px;line-height:13px;color:var(--body)}
.intro p+p{margin-top:13px}
.read-more{display:flex;align-items:center;gap:8px;font-size:8.6px;color:var(--accent);text-transform:uppercase}
.photo{background:linear-gradient(#b8c2cc,#8f8f8f 55%,#6a6258)}
.intro-photo{left:620px;top:393px;width:196px;height:150px}

/* services */
.service-head{display:flex;align-items:flex-start;gap:10px;font-size:13.6px;font-weight:500;color:var(--ink);line-height:16px}
.frame{border:1px solid #d6d6d6;padding:3px;background:var(--white)}
.frame div{width:100%;height:100%}
.service-text{font-size:10px;line-height:12.6px;color:var(--body)}

/* testimonials */
.section-title{left:185px;top:798px;font-size:16px;font-weight:500;color:var(--ink)}
.quote-mark{font-family:Georgia,serif;font-size:92px;line-height:1;color:var(--muted);letter-spacing:-6px}
.quote{font-size:10px;line-height:12.4px;color:var(--body);width:236px}
.quote p+p{margin-top:12px}
.author{font-size:10px;color:var(--body);text-align:right}

/* footer */
.site-footer{left:0;top:1013px;width:1000px;height:132px;background:var(--footer)}
.footer-title{font-size:16.5px;font-weight:500;color:var(--white)}
.footer-links{list-style:none;font-family:"Open Sans",Arial,sans-serif;font-size:10px;line-height:12.4px;color:var(--white)}
.signup-input{left:331px;top:1060px;width:159px;height:21px;background:var(--white)}
.signup-btn{left:490px;top:1060px;width:26px;height:21px;background:var(--orange);display:flex;align-items:center;justify-content:center}
.signup-note{left:331px;top:1096px;font-size:9.6px;line-height:12.3px;color:var(--white);font-weight:500}
.address{left:555px;top:1059px;font-size:9.6px;line-height:12.3px;color:var(--white);font-weight:500}
.map{left:723px;top:1060px;width:93px;height:57px;background:linear-gradient(135deg,#e9e6df,#d9d6cc);border:1px solid #fff}
.legal{left:0;top:1145px;width:1000px;height:33px;background:var(--footer-dark);font-size:9.8px;font-weight:500;color:var(--white);padding:11px 0 0 188px}
</style>
</head>
<body>
<div class="page">

  <header>
    <div class="abs topbar"></div>
    <div class="abs contact-item" style="left:515px">
      <svg width="26" height="18" viewBox="0 0 26 18"><rect x="1" y="1" width="24" height="16" fill="none" stroke="#5e7a3c" stroke-width="1.6"/><path d="M1 1 L13 10 L25 1" fill="none" stroke="#5e7a3c" stroke-width="1.6"/></svg>
      <span>sales@resilientbuildtech.com</span>
    </div>
    <div class="abs contact-item" style="left:731px">
      <svg width="22" height="22" viewBox="0 0 22 22"><circle cx="11" cy="11" r="9.5" fill="none" stroke="#5e7a3c" stroke-width="1.6"/><path d="M7.5 6.5c1-.8 1.8-.5 2.3.6l.6 1.3c.3.7 0 1.2-.6 1.6.6 1.3 1.6 2.3 2.9 2.9.4-.6.9-.9 1.6-.6l1.3.6c1.1.5 1.4 1.3.6 2.3-2.2 2.3-9.3-4.4-8.7-8.7z" fill="#5e7a3c"/></svg>
      <span>(610) 555-0148</span>
    </div>
    <nav class="abs mainnav">
      <ul>
        <li>HOME</li><li>PRODUCTS</li><li>ABOUT US</li><li>PRODUCT SPECIFICATIONS</li><li>DESIGN DOCUMENTATION</li><li>CONTACT US</li>
      </ul>
    </nav>
    <div class="abs brand">RBT</div>
  </header>

  <div class="abs hero" role="img" aria-label="Photo of a parent and child holding hands on a beach at sunset, boats on the bay behind them"></div>

  <main>
    <div class="abs panel"></div>
    <h1 class="abs panel-title">REBUILD SAFER, STRONGER, BETTER TO BUILD NEW LASTING MEMORIES</h1>
    <div class="abs rule"></div>
    <div class="abs intro">
      <p>Systems for extending the height of existing piles are not available on today's market.&nbsp; Resilient Build Technologies, LLC (RBT) has developed two systems to allow for Piles to be extended that provide superior structural support without corrosion and maintenance concerns.</p>
      <p>We provided two systems, a complete system, Pile Cap Extension Pylonets, and Pile Splice.&nbsp; These two systems allow a home to be raised by up to 54", higher extensions possible with additional design consideration for lateral support. Shown below is the full Piling Extension system, which connects to the top of the existing pile. The system modular and can be cut to meet specific needs of the home.</p>
    </div>
    <div class="abs read-more" style="left:187px;top:534px">READ MORE <svg width="10" height="10" viewBox="0 0 10 10"><circle cx="5" cy="5" r="4.3" fill="none" stroke="#d8261f" stroke-width="1.3"/><path d="M3 5h3.6M5 3.3 6.8 5 5 6.7" fill="none" stroke="#d8261f" stroke-width="1.3"/></svg></div>
    <div class="abs photo intro-photo" role="img" aria-label="Photo of a shingled beach house raised on new piling extensions"></div>

    <section>
      <h2 class="abs service-head" style="left:188px;top:575px">
        <svg width="17" height="17" viewBox="0 0 17 17"><path d="M8.5 1 16 5H1z" fill="#5e7a3c"/><rect x="2" y="6" width="13" height="8" fill="#5e7a3c"/><rect x="1" y="14.5" width="15" height="2" fill="#5e7a3c"/><path d="M5 7v7M8.5 7v7M12 7v7" stroke="#fff" stroke-width="1"/></svg>
        <span style="margin-top:3px">RAISING A STRUCTURE</span>
      </h2>
      <div class="abs frame" style="left:187px;top:615px;width:182px;height:98px"><div class="photo" role="img" aria-label="Photo of a house lifted on cribbing during raising"></div></div>
      <p class="abs service-text" style="left:187px;top:723px;width:185px">Lorem Ipsum. Proin gravida nibh vel velit auctor aliquet. Aenean sollicitudin, lorem quis bibendum</p>
      <div class="abs read-more" style="left:186px;top:770px">READ MORE <svg width="10" height="10" viewBox="0 0 10 10"><circle cx="5" cy="5" r="4.3" fill="none" stroke="#d8261f" stroke-width="1.3"/><path d="M3 5h3.6M5 3.3 6.8 5 5 6.7" fill="none" stroke="#d8261f" stroke-width="1.3"/></svg></div>

      <h2 class="abs service-head" style="left:405px;top:573px">
        <svg width="26" height="18" viewBox="0 0 26 18"><path d="M2 16h22M4 16A9 9 0 0 1 21 12" fill="none" stroke="#5e7a3c" stroke-width="2"/><path d="M2 2l10 14" stroke="#5e7a3c" stroke-width="2"/><circle cx="12" cy="10" r="2.5" fill="none" stroke="#5e7a3c" stroke-width="1.5"/></svg>
        <span style="margin-top:5px">NEW CONSTRUCTION</span>
      </h2>
      <div class="abs frame" style="left:405px;top:615px;width:186px;height:98px"><div role="img" aria-label="Photo of hands marking up architectural plans" style="background:linear-gradient(135deg,#e8e6e2,#cfcac4 60%,#b8a89a)"></div></div>
      <p class="abs service-text" style="left:405px;top:723px;width:185px">Lorem Ipsum. Proin gravida nibh vel velit auctor aliquet. Aenean sollicitudin, lorem quis bibendum</p>
      <div class="abs read-more" style="left:405px;top:770px">READ MORE <svg width="10" height="10" viewBox="0 0 10 10"><circle cx="5" cy="5" r="4.3" fill="none" stroke="#d8261f" stroke-width="1.3"/><path d="M3 5h3.6M5 3.3 6.8 5 5 6.7" fill="none" stroke="#d8261f" stroke-width="1.3"/></svg></div>

      <h2 class="abs service-head" style="left:621px;top:575px">
        <svg width="20" height="15" viewBox="0 0 20 15"><path d="M3 0v12M8 0v12M13 0v12M18 0v12" stroke="#5e7a3c" stroke-width="2.4"/><rect x="0" y="12.5" width="20" height="2.5" fill="#5e7a3c"/></svg>
        <span style="margin-top:3px;margin-left:4px">PILING REPAIRS AND<br>EXTENSIONS</span>
      </h2>
      <div class="abs frame" style="left:619px;top:615px;width:197px;height:98px"><div role="img" aria-label="Photo of a house resting on repaired and extended pilings" style="background:linear-gradient(#36404c,#4a4038 55%,#7a5a3a)"></div></div>
      <p class="abs service-text" style="left:619px;top:723px;width:185px">Lorem Ipsum. Proin gravida nibh vel velit auctor aliquet. Aenean sollicitudin, lorem quis bibendum</p>
      <div class="abs read-more" style="left:618px;top:770px">READ MORE <svg width="10" height="10" viewBox="0 0 10 10"><circle cx="5" cy="5" r="4.3" fill="none" stroke="#d8261f" stroke-width="1.3"/><path d="M3 5h3.6M5 3.3 6.8 5 5 6.7" fill="none" stroke="#d8261f" stroke-width="1.3"/></svg></div>
    </section>

    <section>
      <h2 class="abs section-title">WHAT ARE SAYING OUR CLIENTS</h2>

      <div class="abs quote-mark" style="left:180px;top:810px">&ldquo;</div>
      <blockquote class="abs quote" style="left:245px;top:850px">
        <p>Lorem Ipsum. Proin gravida nibh vel velit auctor aliquet. Aenean sollicitudin, lorem quis bibendum auctor, nisi elit consequat ipsum, nec sagittis sem nibh id elit.</p>
        <p>Duis sed odio sit amet nibh vulputate cursus a sit amet mauris.</p>
      </blockquote>
      <p class="abs author" style="left:245px;top:958px;width:233px">Tom Harlow - CAPE HATTERAS, NC</p>

      <div class="abs quote-mark" style="left:514px;top:810px">&ldquo;</div>
      <blockquote class="abs quote" style="left:583px;top:850px">
        <p>Lorem Ipsum. Proin gravida nibh vel velit auctor aliquet. Aenean sollicitudin, lorem quis bibendum auctor, nisi elit consequat ipsum, nec sagittis sem nibh id elit.</p>
        <p>Duis sed odio sit amet nibh vulputate cursus a sit amet mauris. Morbi accumsan ipsum velit.</p>
      </blockquote>
      <p class="abs author" style="left:583px;top:958px;width:232px">Mary Linden - MOREHEAD CITY, NC</p>

      <div class="abs read-more" style="left:687px;top:985px;gap:17px">READ MORE TESTIMONIALS <svg width="10" height="10" viewBox="0 0 10 10"><circle cx="5" cy="5" r="4.3" fill="none" stroke="#d8261f" stroke-width="1.3"/><path d="M3 5h3.6M5 3.3 6.8 5 5 6.7" fill="none" stroke="#d8261f" stroke-width="1.3"/></svg></div>
    </section>
  </main>

  <footer>
    <div class="abs site-footer"></div>
    <h3 class="abs footer-title" style="left:186px;top:1029px">COMPANY</h3>
    <ul class="abs footer-links" style="left:186px;top:1058px">
      <li>Home</li><li>Products</li><li>About Us</li><li>Product Specifications</li><li>Design Documentation</li><li>Contact Us</li>
    </ul>
    <h3 class="abs footer-title" style="left:331px;top:1029px">EMAIL SIGN UP</h3>
    <div class="abs signup-input"></div>
    <div class="abs signup-btn"><svg width="12" height="10" viewBox="0 0 12 10"><path d="M0 5h10M6 1l4 4-4 4" fill="none" stroke="#fff" stroke-width="1.8"/></svg></div>
    <p class="abs signup-note">Sign up and we'll keep you updated<br>with the latest RBT updates and news</p>
    <h3 class="abs footer-title" style="left:555px;top:1029px">CONNECT</h3>
    <address class="abs address" style="font-style:normal">PO Box 4410<br>Lehigh Valley<br>PA 18002-0000<br>Phone: (610) 555-0148<br>sales@resilientbuildtech.com</address>
    <div class="abs map" role="img" aria-label="Small street map showing the office location"></div>
    <div class="abs legal">Copyright © 2013&nbsp; RESILIENT BUILD TECHNOLOGIES, LLC&nbsp; All Rights Reserved</div>
  </footer>

</div>
</body>
</html>
```